Brochure Design Project

This will be a tri-fold full 8.5x11 brochure that will be distributed and sitting in Oncology offices all throughout the US. It is a lead generation and referral designed piece that it to target all patients, Cancer primarily, but all critically ill patients and seniors above the age of 70. We want our service to go beyond just a financial transaction, we want to educate patients of their rights within a life insurance policy and if we cannot help them personally, do want to assist them by referring them to other agencies and non profits than can. ( I want to redesign the brochure attached, it can be very similar and need only minor changes to content, but would welcome all suggestions on improving message, and in gaining attention, picture substitutions and change of colors, along with the layout itself can be improved upon, and I need this piece to look very professional and appropriate for medical offices. I will be needing assistance on several upcoming projects and will also have great printing demands.

Target Market(s)

Cancer patients
all chronically and critically ill patients
all seniors above age 70

Industry/Entity Type

Life Insurance

Requirements
Must have
• Cancer and the terminally ill
Nice to have
• seniors above 70

```html
<!DOCTYPE html>
<html lang="en">
<head>
<meta charset="utf-8">
<title>Lumen Settlements – Tri-Fold Brochure Inside</title>
<link rel="stylesheet" href="https://fonts.googleapis.com/css2?family=Arimo:ital,wght@0,400;0,700;1,400;1,700&family=Dancing+Script:wght@600&display=swap">
<style>
  :root{
    --paper:#ffffff;
    --backdrop:#e9ebee;
    --brand-blue:#0b5fae;
    --logo-blue:#2b7fd6;
    --ink:#1e1e1e;
    --ink-soft:#3a3a3a;
    --rule:#444;
    --dash:#5b93cf;
    --script:#1f6cc0;
  }
  *{box-sizing:border-box;margin:0;padding:0}
  html,body{width:1200px;height:955px;overflow:hidden;background:var(--backdrop)}
  body{font-family:"Arimo",Arial,sans-serif;color:var(--ink);position:relative}

  .brochure{
    position:absolute;left:30px;top:36px;width:645px;height:499px;
    background:var(--paper);transform:scale(1.7674);transform-origin:0 0;
    box-shadow:0 1px 3px rgba(0,0,0,.25);overflow:hidden;
  }
  .abs{position:absolute}

  /* photo areas */
  .photo{position:absolute;overflow:hidden}
  .photo--couple{left:16px;top:39px;width:194px;height:194px;border-radius:10px;border:1px solid #333;
    background:linear-gradient(160deg,#e9e2d4 0%,#c8d6df 45%,#8fb7c4 100%)}
  .photo--pills{left:148px;top:158px;width:112px;height:137px;border-radius:8px;border:1px solid #333;
    background:linear-gradient(170deg,#8d5a3c 0%,#c89a78 45%,#e6a456 100%)}
  .photo--doctor{left:225px;top:0;width:195px;height:233px;border-bottom-right-radius:10px;border:1px solid #333;border-top:none;
    background:linear-gradient(150deg,#ececea 0%,#d9dadc 40%,#b9c3cc 100%)}

  .call-box{left:262px;top:243px;width:148px;height:38px;background:var(--brand-blue);border-radius:6px;
    color:#fff;text-align:center;padding-top:4px}
  .call-box__phone{font-size:13px;font-weight:700;line-height:1.1}
  .call-box__phone small{font-size:11px}
  .call-box__web{font-size:8.5px;font-weight:700;line-height:1.3}

  .brand-name{color:var(--logo-blue);font-weight:700;text-align:center;white-space:nowrap}
  .brand-name--left{left:24px;top:248px;width:118px;font-size:9.5px;letter-spacing:1.2px;line-height:1.25}
  .brand-name--left span{display:block}

  .money-head{left:0;top:297px;width:225px;text-align:center;font-size:14px;font-style:italic;font-weight:700}
  .money-head b{font-style:normal;font-size:20px;font-weight:700}
  .questions{left:17px;top:330px;width:195px;font-size:8.6px;font-style:italic;line-height:1.25;color:var(--ink-soft)}
  .questions p{margin-bottom:8px}

  .band{left:0;top:466px;width:433px;height:32px;background:var(--brand-blue);color:#fff;
    font-size:10.4px;font-weight:700;text-align:center;line-height:32px}

  .reality-head{left:225px;top:296px;width:208px;text-align:center;line-height:1}
  .reality-head__line1{font-size:14px}
  .reality-head__line1 em{font-size:19px;font-weight:700}
  .reality-head__line2{font-size:20px;font-weight:700;letter-spacing:.5px;margin-top:1px}
  .reality-copy{left:226px;top:345px;width:196px;font-size:8.9px;line-height:1.3;color:var(--ink-soft)}
  .reality-copy p{margin-bottom:7px}
  .tagline{left:225px;top:436px;width:200px;text-align:center;font-family:"Dancing Script",cursive;
    font-size:15px;color:var(--script);white-space:nowrap}

  .eligibility{left:437px;top:12px;width:200px;font-size:8px;font-style:italic;line-height:1.3;color:var(--ink-soft)}
  .eligibility p{margin-bottom:8px}
  .eligible-head{left:433px;top:87px;width:212px;text-align:center;font-size:8.2px;font-weight:700;line-height:1.2}
  .eligible-head span{display:block;font-size:11.5px;margin-top:2px}
  .kit-box{left:433px;top:121px;width:205px;height:49px;border:1px solid var(--dash);border-radius:7px;
    font-size:7.6px;text-align:center;line-height:1.3;padding-top:3px}
  .brand-name--right{left:433px;top:196px;width:212px;font-size:13px;letter-spacing:2px}
  .phone-big{left:433px;top:229px;width:212px;text-align:center;font-size:19px;font-weight:700}

  .form-box{left:433px;top:255px;width:210px;height:238px;border:1px dashed var(--dash)}
  .form-rot{position:absolute;width:238px;height:210px;left:-14px;top:14px;transform:rotate(-90deg);padding:8px 8px 0 6px}
  .form-title{font-size:10px;font-weight:700;margin-bottom:6px}
  .form-title u{text-decoration:underline}
  .field{display:flex;align-items:flex-end;font-size:6.6px;height:17px;color:var(--ink-soft)}
  .field i{flex:1;border-bottom:.6px solid var(--rule);margin-left:3px;height:7px}
  .field .gap{flex:0 0 18px}
  .field-note{font-size:6.4px;margin-top:12px;color:var(--ink-soft)}
  .form-foot{display:flex;align-items:center;justify-content:space-between;margin-top:10px}
  .form-foot .brand-name{font-size:7px;letter-spacing:1px}
  .form-web{font-size:8.5px;font-weight:700}
</style>
</head>
<body>
<main class="brochure">

  <!-- left panel -->
  <div class="photo photo--couple" role="img" aria-label="Photo of a smiling senior couple walking arm in arm at home"></div>
  <div class="photo photo--pills" role="img" aria-label="Photo of a senior man holding a prescription pill bottle"></div>
  <div class="brand-name brand-name--left abs"><span>LUMEN</span><span>SETTLEMENTS</span></div>

  <h2 class="money-head abs">It's <b>YOUR</b> Money</h2>
  <div class="questions abs">
    <p>Why do insurance companies conceal the fact that policy holders may be entitled to additional cash benefits?</p>
    <p>Why are bankruptcy rates among cancer patients and seniors more than double that of the general population?</p>
    <p>Why do patients who are receiving care feel unsure about discussing the subject of MONEY and the effects it can have both emotionally and physically?</p>
  </div>

  <!-- middle panel -->
  <div class="photo photo--doctor" role="img" aria-label="Photo of a doctor examining a senior woman's arm"></div>
  <div class="call-box abs">
    <div class="call-box__phone"><small>call</small> 800-555-0147</div>
    <div class="call-box__web">www.lumensettlements.com</div>
  </div>

  <h2 class="reality-head abs">
    <div class="reality-head__line1">Turning <em>HOPE</em> Into</div>
    <div class="reality-head__line2">REALITY</div>
  </h2>
  <div class="reality-copy abs">
    <p>Everyone on the journey of medical recovery should have access to <b>FINANCIAL SUPPORT</b> that improves quality of life and provides relief from distress.</p>
    <p>We can help provide the information and guidance you need to learn more about the Financial Resources available.</p>
  </div>
  <div class="tagline abs">Discover Financial Freedom!</div>

  <div class="band abs">HEALING &amp; RECOVERY should be the primary concern for all patients...NOT MONEY!</div>

  <!-- right panel -->
  <div class="eligibility abs">
    <p>Have you been diagnosed with a life threatning illness and own life isurance or are covered by a group policy?</p>
    <p>Were you born before 1943 and own life insurance or are covered by a goup policy?</p>
  </div>
  <div class="eligible-head abs">YOU MAY BE ELIGIBLE TO RECEIVE A<span>LUMEN SETTLEMENT</span></div>
  <div class="kit-box abs">
    Call today to receive your <i>FREE</i> &amp; <i>CONFIDENTIAL</i><br>
    <b>Lumen Settlement Kit</b> or ask one of our<br>
    <b>Family Service Counselors</b> for<br>
    assistance or advice on where to turn.
  </div>
  <div class="brand-name brand-name--right abs">LUMEN SETTLEMENTS</div>
  <div class="phone-big abs">800-555-0147</div>

  <section class="form-box abs">
    <div class="form-rot">
      <div class="form-title">Please send me a <u>FREE INFORMATION KIT</u></div>
      <div class="field">Name:<i></i></div>
      <div class="field">Address:<i></i></div>
      <div class="field">City:<i></i></div>
      <div class="field">e-mail:<i></i></div>
      <div class="field">Phone:<i></i></div>
      <div class="field">Best time to call:<i></i>AM<i class="gap"></i>PM<i class="gap"></i></div>
      <div class="field">Insurance Co:<i></i></div>
      <div class="field-note">All communication will be strictly confidential.</div>
      <div class="form-foot">
        <span class="brand-name">LUMEN SETTLEMENTS</span>
        <span class="form-web">www.lumensettlements.com</span>
      </div>
    </div>
  </section>

</main>
</body>
</html>
```